Premium Packaging Design for a Line of Four Beeswax Candle Scents

Need to design a beeswax quality candle design for ceramic and tube packaging. The ceramic jar size is 11oz (311g) and should be on the label with reference to hand poured or hand crafted.
4 scents that match our branding for our incense. Scents are : 1) Maple Thistle 2) Amber Fig 3) Silver Meadow 4) Cardamom Reverie. Each tube must have elements of each of its scents i.e cardamom reverie should make reference to coffee. Die Line for the candle packaging sizing is attached in files. Design is for the tube packaging only. Must include warning label on the bottom with barcode (dummy barcode can be used for design phase). Logo and other design elements can be taken from .ai incense box. Elements of bees such as wax comb or hexagonal shapes should be used.
Bottom Warning Label (text):
1) Warning Triangle should be in Yellow
2) Icons (attached should be used)
3) Wording:
Always burn within sight and never in drafty conditions
Keep away from things that catch fire
Keep away from children and pets
4) Burn Instructions
Trim wick to 1/4" each time candle is lit. Keep wax pool free of debris including matches and wick trimmings. Only burn candle on level fire resistant surface. Do not burn candle for more than 4 hours at a time.

Target Market(s)

USA market. Must have MADE IN USA on packaging

Industry/Entity Type

Health and Beauty

Font styles to use
Decorative
Script

Requirements
Must have
• Gold stamping
Nice to have
• Follow branded guidelines as per our incense box
Should not have
• cheap and generic stock images

```html
<!DOCTYPE html>
<html lang="en">
<head>
<meta charset="UTF-8">
<title>Veyora – Maple Thistle Candle Tube</title>
<link rel="stylesheet" href="https://fonts.googleapis.com/css2?family=EB+Garamond:wght@400;500&display=swap">
<style>
  :root {
    --backdrop: #523470;
    --tube: #2a2a1c;
    --tube-edge: #1c1c13;
    --lid-top: #121210;
    --gold: #d8b65a;
    --gold-light: #f1dc9a;
    --gold-deep: #a5812f;
    --ink-purple: #45287f;
    --ink-light: #ece6d6;
  }
  * { margin: 0; padding: 0; box-sizing: border-box; }
  html, body { width: 1200px; height: 529px; overflow: hidden; background: var(--backdrop); }
  body { font-family: "EB Garamond", Georgia, serif; }
  .canvas { position: relative; width: 1200px; height: 529px; }

  .panel {
    position: absolute;
    top: 98px;
    width: 262px;
    height: 318px;
    background: var(--tube);
    border-radius: 4px;
    box-shadow: 0 10px 24px rgba(20, 8, 35, 0.45);
  }
  .panel--front { left: 138px; }
  .panel--back { left: 430px; }
  .lid-seam {
    position: absolute; left: 0; right: 0; top: 107px;
    height: 2px; background: var(--tube-edge);
  }

  .brand {
    position: absolute; left: 0; right: 0; top: 54px;
    text-align: center;
    font-size: 26px; line-height: 1; font-weight: 500; letter-spacing: 0.04em;
    color: var(--gold);
  }

  .scent-label { position: absolute; left: 36px; top: 133px; width: 190px; height: 170px; }
  .scent-label svg { position: absolute; inset: 0; }
  .scent-text {
    position: absolute; inset: 0;
    display: flex; flex-direction: column; align-items: center;
    color: var(--ink-purple); text-align: center;
  }
  .scent-kicker { margin-top: 28px; font-size: 8.5px; font-weight: 500; letter-spacing: 0.02em; }
  .scent-name { margin-top: 16px; font-size: 24px; line-height: 1; }
  .scent-craft { margin-top: 26px; font-size: 9.5px; }
  .scent-weight { margin-top: 7px; font-size: 5px; letter-spacing: 0.04em; }

  .story {
    position: absolute; left: 30px; right: 30px; top: 130px;
    text-align: center; color: var(--ink-light);
    font-size: 11px; line-height: 14.6px;
  }
  .origin {
    position: absolute; left: 0; right: 0; top: 290px;
    text-align: center; color: var(--ink-light);
    font-size: 10.5px; letter-spacing: 0.02em;
  }

  .lid {
    position: absolute; left: 750px; top: 112px;
    width: 300px; height: 300px; border-radius: 50%;
    background: var(--tube);
    box-shadow: 0 10px 24px rgba(20, 8, 35, 0.45);
    display: flex; align-items: center; justify-content: center;
  }
  .lid-face {
    width: 272px; height: 272px; border-radius: 50%;
    background: var(--lid-top);
    display: flex; align-items: center; justify-content: center;
  }
  .lid-face .brand-mark {
    font-size: 24px; line-height: 1; font-weight: 500; letter-spacing: 0.04em; color: var(--gold);
  }
</style>
</head>
<body>
<main class="canvas">

  <section class="panel panel--front" aria-label="Front of tube">
    <div class="lid-seam"></div>
    <div class="brand">VEYORA</div>
    <div class="scent-label">
      <svg viewBox="0 0 190 170" width="190" height="170" aria-hidden="true">
        <defs>
          <linearGradient id="goldFoil" x1="0" y1="0" x2="1" y2="1">
            <stop offset="0" stop-color="#a5812f"/>
            <stop offset="0.45" stop-color="#f1dc9a"/>
            <stop offset="1" stop-color="#a5812f"/>
          </linearGradient>
        </defs>
        <polygon points="47,2 143,2 188,85 143,168 47,168 2,85" fill="url(#goldFoil)"/>
        <polygon points="50,7 140,7 182,85 140,163 50,163 8,85" fill="none" stroke="#45287f" stroke-width="1.4"/>
      </svg>
      <div class="scent-text">
        <p class="scent-kicker">NATURAL BEESWAX</p>
        <p class="scent-name">MAPLE<br>THISTLE</p>
        <p class="scent-craft">HAND CRAFTED</p>
        <p class="scent-weight">NET WT 11oz (311g)</p>
      </div>
    </div>
  </section>

  <section class="panel panel--back" aria-label="Back of tube">
    <div class="lid-seam"></div>
    <p class="story">Only the highest quality 100%<br>pure American beeswax is<br>sourced by Veyora to create our<br>range of candles, guaranteeing<br>sustainability. Our beeswax<br>candles burn longer and cleaner<br>than traditional candles,<br>releasing a delicate blend of<br>honey-scented fragrance that<br>will transport your senses.</p>
    <p class="origin">PRODUCT OF USA</p>
  </section>

  <section class="lid" aria-label="Top of lid">
    <div class="lid-face">
      <span class="brand-mark">VEYORA</span>
    </div>
  </section>

</main>
</body>
</html>
```